Career development coaching - school lever to adults, needs a business card

Tandem Lark - An independent Career Advice business that provides 1-2-1 advice,for career development, entrepreneurial support and workshops needs a business card. Our clients of all ages (school leaver to adults looking for a career move) and universities and colleges. We would like the card to be double-sided with a modern, professional look. Looking for something professional yet very creative and original. Want a standard size business card that inspires a second look because it stands out from the rest.

One side of the card to have a design incorporating the logo with Tandem Lark name with the strap line “Guiding every next step ahead” and space for the company website

Other side of the card to the logo/Tandem Lark name and the usual contact information:
Individual Name
Job Title (for example, Director)
Phone number
Email address
Company website address

Facebook, LinkedIn and Twitter links will need to go somewhere (back or front!)

The design will be used for 3 individuals so should be editable so that we can update as needed/as we grow.

Attached is the company logo/colours to be incorporated.

Target Market(s)

1-2-1 advice,for career development, entrepreneurial support and workshops needs a business card. Our clients of all ages (school leaver to adults looking for a career move) and universities and colleges.

Industry/Entity Type

Consulting

Contact Information for Business Card

Individual Name
Phone number
Email address
Company website address

Font styles to use
Sans Serif

Colors
0255a3
3176b5
faa54b
f78f20
85acd3
cfdeed

Requirements
Must have
• use the Tandem Lark Logo in some way - using the colours and the blue/orange palette
• For the logo - hope this makes sense to someone or if they direclty relate to the logo image attached!
• For the Orange:- Pantone 1585 C
• In CMYK : C3 M71 Y100 K0
• For the Blue:- 100% Pantone 7469 C
• In CMYK : C100 M62 Y27 K7
• Please feel free to contact me with any questions for more info
Nice to have
• happy to see any creative designs
Should not have
• Nothing too traditional,

```html
<!DOCTYPE html>
<html lang="en">
<head>
<meta charset="utf-8">
<title>Tandem Lark – Business Card</title>
<link href="https://fonts.googleapis.com/css2?family=Open+Sans:wght@400;600&display=swap" rel="stylesheet">
<style>
  :root {
    --orange: #ec7035;
    --blue: #0e6591;
    --white: #ffffff;
    --backdrop: #ecebe8;
    --divider: rgba(255,255,255,0.7);
  }
  * { margin: 0; padding: 0; box-sizing: border-box; }
  html, body {
    width: 1200px; height: 900px; overflow: hidden;
    background: var(--backdrop);
    font-family: "Open Sans", Arial, sans-serif;
  }
  .sheet {
    width: 1200px; height: 900px;
    display: flex; flex-direction: column; align-items: center; justify-content: center;
    gap: 40px;
  }
  .card {
    width: 700px; height: 400px; position: relative; overflow: hidden;
    box-shadow: 0 6px 18px rgba(0,0,0,0.18);
  }

  /* Front */
  .card--front {
    background: var(--orange);
    display: flex; flex-direction: column; align-items: center; justify-content: center;
    color: var(--white);
  }
  .brand { display: flex; align-items: center; gap: 14px; }
  .brand__dot { width: 22px; height: 22px; border-radius: 50%; }
  .brand__name { font-weight: 600; text-transform: uppercase; letter-spacing: 2px; white-space: nowrap; }
  .card--front .brand__dot { background: var(--blue); }
  .card--front .brand__name { color: var(--blue); font-size: 38px; }
  .tagline {
    margin-top: 26px; font-size: 19px; letter-spacing: 1px; text-transform: uppercase;
  }

  /* Back */
  .card--back { background: var(--white); }
  .back__identity {
    height: 190px; display: flex; align-items: center; justify-content: center;
  }
  .card--back .brand__dot { background: var(--orange); width: 26px; height: 26px; }
  .card--back .brand__name { color: var(--blue); font-size: 40px; }
  .back__role {
    position: absolute; top: 190px; left: 0; width: 100%; height: 76px;
    background: var(--blue); color: var(--white);
    display: flex; align-items: center;
  }
  .role__name {
    width: 50%; text-align: right; padding-right: 22px;
    font-size: 25px; font-weight: 600;
  }
  .role__title {
    width: 50%; padding-left: 22px; font-size: 17px;
    border-left: 1px solid var(--divider); line-height: 44px;
  }
  .back__contact {
    position: absolute; top: 272px; left: 0; width: 100%; height: 128px;
    background: var(--orange); color: var(--white);
    display: flex; align-items: center;
  }
  .contact__list, .social__list { list-style: none; font-size: 18px; line-height: 30px; white-space: nowrap; }
  .contact__list {
    width: 50%; padding-right: 22px; text-align: right;
  }
  .contact__list li { display: flex; justify-content: flex-end; align-items: center; gap: 8px; }
  .contact__list svg { width: 15px; height: 15px; }
  .social__list {
    width: 50%; padding-left: 22px; border-left: 1px solid var(--divider);
  }
  .social__list li { display: flex; align-items: center; gap: 8px; }
  .social__mark { width: 14px; height: 14px; background: var(--white); border-radius: 2px; }
</style>
</head>
<body>
<main class="sheet">

  <section class="card card--front" aria-label="Business card front">
    <div class="brand">
      <span class="brand__dot"></span>
      <span class="brand__name">Tandem Lark</span>
    </div>
    <p class="tagline">Guiding every next step ahead</p>
  </section>

  <section class="card card--back" aria-label="Business card back">
    <div class="back__identity">
      <div class="brand">
        <span class="brand__dot"></span>
        <span class="brand__name">Tandem Lark</span>
      </div>
    </div>

    <div class="back__role">
      <p class="role__name">Marcus Hale</p>
      <p class="role__title">Managing Director</p>
    </div>

    <div class="back__contact">
      <ul class="contact__list">
        <li>(044) 555 010 233
          <svg viewBox="0 0 16 16" aria-hidden="true"><path fill="#fff" d="M3 2h3l1.5 3.5-2 1.3a8 8 0 0 0 3.7 3.7l1.3-2L14 10v3a1 1 0 0 1-1 1A11 11 0 0 1 2 3a1 1 0 0 1 1-1z"/></svg>
        </li>
        <li>hello@tandemlark.com
          <svg viewBox="0 0 16 16" aria-hidden="true"><rect x="1.5" y="3.5" width="13" height="9" fill="none" stroke="#fff" stroke-width="1.4"/><path d="M1.5 3.5 8 9l6.5-5.5" fill="none" stroke="#fff" stroke-width="1.4"/></svg>
        </li>
        <li>www.tandemlark.com
          <svg viewBox="0 0 16 16" aria-hidden="true"><path d="M6.5 9.5l3-3M7 4.5l1.5-1.5a2.5 2.5 0 0 1 3.5 3.5L10.5 8M9 11.5 7.5 13A2.5 2.5 0 0 1 4 9.5L5.5 8" fill="none" stroke="#fff" stroke-width="1.4" stroke-linecap="round"/></svg>
        </li>
      </ul>
      <ul class="social__list">
        <li><span class="social__mark"></span>friendloop.net/tandemlark</li>
        <li><span class="social__mark"></span>workgrid.net/tandemlark</li>
        <li><span class="social__mark"></span>chirpline.net/tandemlark</li>
      </ul>
    </div>
  </section>

</main>
</body>
</html>
```